Professional IT Company Letterhead

We need a new letterhead design to incorporate our new login and business card design recently received here on Sketch Guild. We want the same look and feel as the other two accepted projects. We want a professional and clean design.

Target Market(s)

Medical/Dental and Professional Services Businesses (CPA, Attorney, Architect etc)

Industry/Entity Type

Business

Requirements
Must have
• Clean and professional, consistent brand with our current design of our new logo and business cards.
Nice to have
• Would like to also be able to use the design on our newsletter header

```html
<!DOCTYPE html>
<html lang="en">
<head>
<meta charset="utf-8">
<title>Tidewell Technology Letterhead</title>
<link rel="stylesheet" href="https://fonts.googleapis.com/css2?family=PT+Sans:wght@400;700&family=Quicksand:wght@500&display=swap">
<style>
  :root {
    --brand-blue: #1b75bb;
    --sky-blue: #29a9e1;
    --water-light: #d6ecf9;
    --water-mid: #8cc6ea;
    --text-grey: #4a4a4a;
    --paper: #ffffff;
  }
  * { margin: 0; padding: 0; box-sizing: border-box; }
  html, body { width: 840px; height: 1200px; overflow: hidden; background: var(--paper); }
  .letterhead {
    position: relative;
    width: 840px;
    height: 1200px;
    background: var(--paper);
    font-family: "PT Sans", Arial, sans-serif;
    color: var(--text-grey);
  }
  .brand {
    position: absolute;
    left: 124px;
    top: 112px;
    width: 310px;
  }
  .brand-name {
    font-weight: 700;
    font-size: 34px;
    line-height: 1;
    color: var(--brand-blue);
    white-space: nowrap;
    letter-spacing: -0.3px;
  }
  .brand-tagline {
    margin-top: 38px;
    font-family: "Quicksand", Arial, sans-serif;
    font-weight: 500;
    font-size: 12.5px;
    letter-spacing: 1px;
    color: var(--sky-blue);
    white-space: nowrap;
  }
  .sender {
    position: absolute;
    left: 555px;
    top: 105px;
    height: 61px;
    padding-left: 21px;
    border-left: 2px solid var(--brand-blue);
  }
  .sender-name {
    font-size: 26px;
    line-height: 1.1;
    color: var(--brand-blue);
    padding-top: 4px;
    white-space: nowrap;
  }
  .sender-role {
    font-size: 14px;
    margin-top: 3px;
    color: var(--text-grey);
    white-space: nowrap;
  }
  .mascot {
    position: absolute;
    left: 78px;
    top: 915px;
    width: 142px;
    height: 90px;
    border-radius: 12px;
    background: var(--water-light);
  }
  .water-band {
    position: absolute;
    left: 0;
    top: 1008px;
    width: 840px;
    height: 52px;
    background: linear-gradient(to bottom, var(--water-light), var(--water-mid) 50%, var(--water-light));
  }
  .contact {
    position: absolute;
    top: 1064px;
    left: 0;
    width: 840px;
    height: 60px;
    font-size: 10.5px;
    font-weight: 700;
    line-height: 12.5px;
    color: var(--text-grey);
  }
  .contact-lines {
    position: absolute;
    right: 449px;
    top: 7px;
    text-align: right;
  }
  .contact-line {
    display: flex;
    justify-content: flex-end;
    align-items: center;
    gap: 7px;
    white-space: nowrap;
  }
  .contact-line svg { width: 10px; height: 10px; display: block; }
  .contact-address {
    position: absolute;
    left: 399px;
    top: 0;
    height: 58px;
    padding-left: 7px;
    padding-top: 7px;
    border-left: 1.5px solid var(--brand-blue);
    white-space: nowrap;
  }
</style>
</head>
<body>
<main class="letterhead">
  <header class="brand">
    <div class="brand-name">Tidewell Technology</div>
    <div class="brand-tagline">IT Support for Medical &amp; Dental Practices</div>
  </header>

  <section class="sender">
    <div class="sender-name">Dana Marsh</div>
    <div class="sender-role">President and CEO</div>
  </section>

  <div class="mascot" role="img" aria-label="Cartoon fish mascot illustration"></div>

  <div class="water-band" role="img" aria-label="Water splash illustration spanning the page"></div>

  <footer class="contact">
    <div class="contact-lines">
      <div class="contact-line">281 555 0142
        <svg viewBox="0 0 12 12" aria-hidden="true"><rect width="12" height="12" rx="1.5" fill="var(--brand-blue)"/><path d="M3.5 2.5 h2 v2 l-1 1 a5 5 0 0 0 2 2 l1 -1 h2 v2 a1 1 0 0 1 -1 1 a6 6 0 0 1 -6 -6 a1 1 0 0 1 1 -1 z" fill="#fff"/></svg>
      </div>
      <div class="contact-line">281 555 0187
        <svg viewBox="0 0 12 12" aria-hidden="true"><rect width="12" height="12" rx="1.5" fill="var(--brand-blue)"/><rect x="3" y="2" width="6" height="3" fill="#fff"/><rect x="2" y="5.5" width="8" height="4.5" rx="0.8" fill="#fff"/></svg>
      </div>
      <div class="contact-line">www.tidewellsystems.com</div>
    </div>
    <div class="contact-address">
      dmarsh@tidewellsystems.com<br>
      2280 Maple Ridge Lane, Ste. B<br>
      Riverton, Texas 77410
    </div>
  </footer>
</main>
</body>
</html>
```